Print Ad Design

I need an ad designed to promote an event that we are hosting at a trade show for placement in the show program. The art must be ready to submit to the publication by Friday, November 15th at the latest. The ad is 1/2 page in the show program that will be 4.25"X 5.5" and must be submitted as a high resolution (300dpi) PDF. Ad is full colour. The minimum bleed and trim marks are 0.25". The trade show is the Northern Herd Fair in Canada and we would like to promote a 2 day training we will be hosting at the close of the show. Our company is PastureWise Partners - Ultrasound and Diagnostics and the details that should be included in the ad are:
YOU CAN USE ULTRASOUND TO MANAGE YOUR PREG CHECKS
On Farm Ultrasound Training for Producers
When - Friday, Feb. 7th & Saturday, Feb. 8th
9 AM - 5 PM
Where - close to Herd FAIR
Lunch provided
Registration $175 per day - $300 total
Introduction to ultrasound
Reproductive system anatomy
Pregnancy diagnosis
Live on farm scanning demonstrations and practice with case discussions
Tuition redeemable towards the purchase of ultrasound system.
TO REGISTER OR LEARN MORE
email - info@pasturewisepartners.ca or call 1-800-431-5067
(I have attached our logo and some possible images to use in the ad)
Please note that the primary logo to feature is PastureWise Partners and the secondary logo to use in the ad is Veloskar Ultrasound Scanners.
THANK YOU!!!
Target Market(s)
Dairy Farmers (men and women)
Industry/Entity Type
Trade

```html
<!DOCTYPE html>
<html lang="en">
<head>
<meta charset="utf-8">
<title>On Farm Ultrasound Training for Producers</title>
<link rel="stylesheet" href="https://fonts.googleapis.com/css2?family=Bebas+Neue&family=Source+Sans+3:ital,wght@0,300;0,400;0,600;0,700;1,400&display=swap">
<style>
  :root {
    --ink-blue: #1f5d8a;
    --ink-grey: #6b6b73;
    --headline: #dff6f5;
    --photo-dark: #3a3a40;
    --photo-mid: #8c8f96;
    --photo-light: #c9ccd1;
    --circle-teal: #7fd6c4;
    --brand-yellow: #f2c318;
    --brand-blue: #1c66a8;
    --paper: #ffffff;
  }
  * { margin: 0; padding: 0; box-sizing: border-box; }
  html, body { width: 927px; height: 1200px; overflow: hidden; background: var(--paper); }
  .ad {
    position: relative;
    width: 927px;
    height: 1200px;
    background: var(--paper);
    font-family: "Source Sans 3", sans-serif;
    overflow: hidden;
  }
  .hero-photo {
    position: absolute;
    left: 0; top: 0;
    width: 927px; height: 544px;
    background:
      radial-gradient(ellipse at 70% 60%, var(--photo-light) 0%, transparent 45%),
      radial-gradient(ellipse at 45% 35%, #3b5f9a 0%, transparent 40%),
      linear-gradient(135deg, #5b4a3a 0%, var(--photo-dark) 40%, var(--photo-mid) 75%, #d9dcdf 100%);
  }
  .headline {
    position: absolute;
    left: 40px; top: 142px;
    width: 300px;
    font-family: "Bebas Neue", sans-serif;
    font-size: 53px;
    line-height: 48px;
    text-align: center;
    color: var(--headline);
    letter-spacing: 0.5px;
    text-shadow: 0 0 10px rgba(0,0,0,0.55), 0 0 3px rgba(0,0,0,0.6);
  }
  .inset-photo {
    position: absolute;
    left: 40px; top: 428px;
    width: 294px; height: 294px;
    border-radius: 50%;
    border: 4px solid var(--paper);
    background:
      radial-gradient(circle at 60% 55%, #2c2c30 0%, transparent 30%),
      linear-gradient(120deg, var(--circle-teal) 0%, #b9efe2 45%, #6d5f58 75%, #e4e1de 100%);
  }
  .details {
    position: absolute;
    left: 340px; top: 568px;
    width: 560px;
    text-align: center;
    color: var(--ink-grey);
  }
  .title {
    font-weight: 300;
    font-size: 51px;
    line-height: 54px;
    color: var(--ink-blue);
    margin-bottom: 22px;
  }
  .when, .where { font-size: 23px; line-height: 32px; }
  .where { margin-bottom: 26px; }
  .program { font-size: 21px; line-height: 29px; margin-bottom: 18px; }
  .tuition { font-style: italic; font-size: 21px; line-height: 31px; margin-bottom: 20px; }
  .cta-label { font-weight: 600; font-size: 21px; line-height: 28px; color: var(--ink-blue); }
  .contact { font-size: 21px; line-height: 30px; }
  .partner-logos {
    position: absolute;
    left: 385px; top: 1118px;
    width: 470px; height: 56px;
    display: flex;
    align-items: center;
    justify-content: space-between;
  }
  .logo {
    display: flex;
    align-items: center;
    gap: 10px;
    font-family: "Source Sans 3", sans-serif;
    font-weight: 600;
    font-size: 22px;
    line-height: 24px;
  }
  .logo-primary { color: var(--brand-blue); }
  .logo-secondary { color: var(--ink-blue); }
  .logo-mark { flex: none; }
</style>
</head>
<body>
<main class="ad">
  <div class="hero-photo" role="img" aria-label="Photo of two technicians with portable ultrasound scanners performing a pregnancy check on a dairy cow"></div>
  <h1 class="headline">You can use<br>ultrasound<br>to manage<br>your preg<br>checks</h1>
  <div class="inset-photo" role="img" aria-label="Close-up photo of a handheld ultrasound scanner in use beside a cow"></div>

  <section class="details">
    <h2 class="title">On Farm Ultrasound<br>Training for Producers</h2>
    <p class="when">Friday, Feb. 7th &amp; Saturday, Feb. 8th, 9 AM - 5 PM</p>
    <p class="where">@ close to Herd FAIR</p>
    <p class="program">Lunch provided | Registration $175 per day - $300 total<br>Introduction to ultrasound | Reproductive system<br>anatomy | Pregnancy diagnosis | Live on farm scanning<br>demonstrations and practice with case discussions</p>
    <p class="tuition">Tuition redeemable towards the purchase of ultrasound<br>system.</p>
    <p class="cta-label">TO REGISTER OR LEARN MORE</p>
    <p class="contact">email - info@pasturewisepartners.ca or call 1-800-431-5067</p>
  </section>

  <footer class="partner-logos">
    <div class="logo logo-primary">
      <svg class="logo-mark" width="34" height="34" viewBox="0 0 34 34" aria-hidden="true"><circle cx="17" cy="17" r="16" fill="var(--brand-yellow)"/></svg>
      <span>PastureWise<br>Partners</span>
    </div>
    <div class="logo logo-secondary">
      <svg class="logo-mark" width="30" height="30" viewBox="0 0 30 30" aria-hidden="true"><rect width="30" height="30" fill="var(--brand-yellow)"/></svg>
      <span>Veloskar<br>Ultrasound Scanners</span>
    </div>
  </footer>
</main>
</body>
</html>
```